Business cards for Remote DBA team

Business cards for team offering database administration, consultation, machine learning and AI services. As of now team is using both
www.fenrowlabs.cz and www.quillbarkgroup.cz URLs

Target Market(s)

IT managers

Industry/Entity Type

It Professional

Contact Information for Business Card

Should include logo
name, email, phone, twitter tag

Font styles to use
Sans Serif

Colors

Designer to choose colors to be used in the design.

```html
<!DOCTYPE html>
<html lang="en">
<head>
<meta charset="utf-8">
<title>Northgrid Data – Business Cards</title>
<link href="https://fonts.googleapis.com/css2?family=Roboto:wght@400;700&display=swap" rel="stylesheet">
<style>
  :root {
    --stage: #1a1a1a;
    --white: #ffffff;
    --royal: #0a2cf0;
    --sky: #22a6f2;
    --azure: #1a7ff0;
    --navy: #050b26;
    --midnight: #030614;
    --glow: #3fb6ff;
  }
  * { box-sizing: border-box; margin: 0; padding: 0; }
  html, body {
    width: 1200px; height: 1200px; overflow: hidden;
    background: var(--stage);
    font-family: "Roboto", Arial, sans-serif;
    color: var(--white);
  }
  .canvas { position: relative; width: 1200px; height: 1200px; }
  .card {
    position: absolute; width: 356px; height: 203px; overflow: hidden;
    box-shadow: 0 10px 24px rgba(0,0,0,0.55);
  }
  .card--a { left: 213px; top: 367px; }
  .card--b { left: 596px; top: 367px; }
  .card--c { left: 213px; top: 598px; }
  .card--d { left: 596px; top: 598px; }

  .card__art { position: absolute; inset: 0; }
  .card--a .card__art { background: linear-gradient(115deg, var(--royal) 0%, #1450f2 50%, var(--sky) 100%); }
  .card--b .card__art {
    background:
      radial-gradient(ellipse 120px 80px at 6% 48%, rgba(220,245,255,0.95) 0%, rgba(63,182,255,0.6) 35%, rgba(10,40,160,0) 100%),
      linear-gradient(90deg, #0b2a9a 0%, var(--navy) 55%, var(--midnight) 100%);
  }
  .card--c .card__art { background: linear-gradient(120deg, var(--sky) 0%, var(--azure) 55%, #0a3ce8 100%); }
  .card--d .card__art {
    background:
      radial-gradient(ellipse 70px 22px at 50% 92%, rgba(210,240,255,0.95) 0%, rgba(63,182,255,0.5) 45%, rgba(10,40,160,0) 100%),
      radial-gradient(ellipse 140px 110px at 50% 60%, rgba(30,90,230,0.45) 0%, rgba(5,11,38,0) 100%),
      var(--midnight);
  }

  .brand {
    position: absolute; display: flex; align-items: center; gap: 7px;
  }
  .brand__dot { width: 9px; height: 9px; border-radius: 50%; background: var(--white); flex: none; }
  .brand__name {
    font-weight: 700; font-size: 16px; line-height: 15px; letter-spacing: 0.3px;
    color: var(--white); text-transform: uppercase;
  }
  .card--a .brand { left: 30px; top: 104px; }
  .card--b .brand { left: 224px; top: 24px; }
  .card--b .brand__name, .card--d .brand__name { font-size: 14px; line-height: 13px; }
  .card--c .brand { left: 198px; top: 22px; }
  .card--d .brand { left: 30px; top: 24px; }

  .person { position: absolute; }
  .person__name { font-weight: 700; font-size: 14px; letter-spacing: 0.2px; line-height: 16px; }
  .person__role { font-size: 9px; line-height: 12px; margin-top: 2px; padding-left: 2px; }
  .card--a .person { left: 207px; top: 43px; }
  .card--b .person { left: 202px; top: 117px; }
  .card--c .person { left: 43px; top: 126px; }
  .card--d .person { left: 192px; top: 118px; }

  .links { font-size: 8.5px; line-height: 12px; }
  .card--a .links { position: absolute; left: 32px; top: 160px; }
  .person .links { margin-top: 6px; padding-left: 2px; }
  .links--vertical {
    position: absolute; left: 334px; top: 12px;
    transform-origin: 0 0; transform: rotate(90deg) translateY(-100%);
    display: flex; flex-direction: column; gap: 0;
    white-space: nowrap;
  }
  .links--vertical span { display: block; width: 180px; }
</style>
</head>
<body>
<main class="canvas">

  <section class="card card--a">
    <div class="card__art" role="img" aria-label="Abstract blue low-poly geometric background"></div>
    <div class="person">
      <p class="person__name">DANIELA HORVAT</p>
      <p class="person__role">IT technician</p>
    </div>
    <div class="brand">
      <span class="brand__dot"></span>
      <p class="brand__name">Northgrid<br>Data</p>
    </div>
    <div class="links">
      <p>www.fenrowlabs.cz</p>
      <p>www.quillbarkgroup.cz</p>
    </div>
  </section>

  <section class="card card--b">
    <div class="card__art" role="img" aria-label="Dark navy tech background with a bright blue light burst on the left"></div>
    <div class="brand">
      <span class="brand__dot"></span>
      <p class="brand__name">Northgrid<br>Data</p>
    </div>
    <div class="person">
      <p class="person__name">DANIELA HORVAT</p>
      <p class="person__role">IT technician</p>
      <div class="links">
        <p>www.fenrowlabs.cz</p>
        <p>www.quillbarkgroup.cz</p>
      </div>
    </div>
  </section>

  <section class="card card--c">
    <div class="card__art" role="img" aria-label="Light blue background with circuit board traces"></div>
    <div class="brand">
      <span class="brand__dot"></span>
      <p class="brand__name">Northgrid<br>Data</p>
    </div>
    <div class="person">
      <p class="person__name">DANIELA HORVAT</p>
      <p class="person__role">IT technician</p>
    </div>
    <div class="links links--vertical">
      <span>www.fenrowlabs.cz</span>
      <span>www.quillbarkgroup.cz</span>
    </div>
  </section>

  <section class="card card--d">
    <div class="card__art" role="img" aria-label="Dark background with glowing blue light rising from a bright point"></div>
    <div class="brand">
      <span class="brand__dot"></span>
      <p class="brand__name">Northgrid<br>Data</p>
    </div>
    <div class="person">
      <p class="person__name">DANIELA HORVAT</p>
      <p class="person__role">IT technician</p>
      <div class="links">
        <p>www.fenrowlabs.cz</p>
        <p>www.quillbarkgroup.cz</p>
      </div>
    </div>
  </section>

</main>
</body>
</html>
```